Graphic Design Project

I am in need of creating a water bottle label that is clean, simple, Brixo like, and transparent partially. It most contain the following logo at the top, attached. The address presented may or may not stay. I am looking for something that will remind of water, purity, water droplets. Something nice an clean as refreshing water.

Target Market(s)

Hospital system patients

Industry/Entity Type

Graphic Design

Requirements
Nice to have
• Water drops

Wet

Bluish colors

```html
<!DOCTYPE html>
<html lang="en">
<head>
<meta charset="utf-8">
<title>Hospital Vista Serena – Water Label Options</title>
<link rel="stylesheet" href="https://fonts.googleapis.com/css2?family=Cabin:wght@500;700&family=Arimo:wght@700&display=swap">
<style>
  :root {
    --ink: #2b3e92;
    --frame: #3b57a6;
    --label-top: #eef2f5;
    --label-bottom: #dfe7ee;
    --water-night: #163a8c;
    --leaf: #5aa83a;
    --white: #ffffff;
  }
  * { box-sizing: border-box; margin: 0; padding: 0; }
  html, body { width: 1200px; height: 1000px; overflow: hidden; }
  body { position: relative; font-family: "Cabin", sans-serif; color: var(--ink); }

  .board-backdrop {
    position: absolute; inset: 0;
    background: radial-gradient(ellipse at 40% 40%, #eef2f4 0%, #d6dfe4 55%, #b9c6cf 100%);
  }
  .option-number {
    position: absolute; width: 40px; text-align: center;
    font: 500 36px "Cabin", sans-serif; color: var(--frame);
  }

  .label {
    position: absolute; width: 388px; height: 216px; overflow: hidden;
    border: 1px solid var(--frame);
    background: linear-gradient(180deg, var(--label-top), var(--label-bottom));
  }
  .label .water { position: absolute; left: 0; top: 0; width: 100%; height: 100%; }

  .brand-dot {
    position: absolute; left: 86px; top: 4px; width: 60px; height: 60px;
    border-radius: 50%; background: var(--leaf);
  }
  .brand-name {
    position: absolute; left: 90px; top: 62px; width: 240px;
    font: 500 25px/27px "Cabin", sans-serif; color: var(--ink); letter-spacing: 0.5px;
    white-space: nowrap;
  }
  .brand-name span { display: block; }
  .brand-name span:first-child { padding-left: 56px; }

  .product-name {
    position: absolute; left: 0; width: 100%; text-align: center; white-space: nowrap;
    font: 700 22px "Cabin", sans-serif; color: var(--ink);
    text-shadow: 0 0 2px var(--white), 0 0 3px var(--white), 0 0 4px var(--white);
  }
  .product-name.on-deep { color: var(--white); text-shadow: 0 0 3px var(--water-night), 0 0 2px var(--ink); }

  .volume { position: absolute; font: 700 11px "Arimo", sans-serif; color: var(--ink); white-space: nowrap; }
  .volume.on-deep { color: var(--white); }

  .address { position: absolute; font: 700 9px/13px "Arimo", sans-serif; color: var(--ink); white-space: nowrap; }
</style>
</head>
<body>

<svg width="0" height="0" style="position:absolute" aria-hidden="true">
  <defs>
    <linearGradient id="wave-light" x1="0" y1="0" x2="0" y2="1">
      <stop offset="0" stop-color="#ffffff" stop-opacity="0.9"/>
      <stop offset="0.4" stop-color="#a9cdee"/>
      <stop offset="1" stop-color="#dcebf7"/>
    </linearGradient>
    <linearGradient id="wave-blue" x1="0" y1="0" x2="0" y2="1">
      <stop offset="0" stop-color="#e6f1fa"/>
      <stop offset="0.5" stop-color="#7fb6e6"/>
      <stop offset="1" stop-color="#2f6fc2"/>
    </linearGradient>
    <linearGradient id="wave-deep" x1="0" y1="0" x2="0" y2="1">
      <stop offset="0" stop-color="#cfe5f6"/>
      <stop offset="0.45" stop-color="#3a86d2"/>
      <stop offset="1" stop-color="#163a8c"/>
    </linearGradient>
    <linearGradient id="wave-clear" x1="0" y1="0" x2="0" y2="1">
      <stop offset="0" stop-color="#9fc4df"/>
      <stop offset="0.3" stop-color="#e3eef6"/>
      <stop offset="1" stop-color="#c3dbef"/>
    </linearGradient>
  </defs>
</svg>

<div class="board-backdrop" role="img" aria-label="Soft rippling water surface backdrop"></div>

<div class="option-number" style="left:72px;top:106px">1</div>
<div class="option-number" style="left:72px;top:366px">2</div>
<div class="option-number" style="left:72px;top:612px">3</div>
<div class="option-number" style="left:72px;top:842px">4</div>
<div class="option-number" style="left:1092px;top:100px">5</div>
<div class="option-number" style="left:1076px;top:366px">6</div>
<div class="option-number" style="left:1076px;top:612px">7</div>
<div class="option-number" style="left:1076px;top:842px">8</div>

<!-- Option 1 -->
<section class="label" style="left:145px;top:39px">
  <svg class="water" viewBox="0 0 388 216" role="img" aria-label="Curling clear water wave with droplets">
    <path d="M0 92 C70 70 140 110 210 118 C280 126 330 90 388 150 L388 216 L0 216 Z" fill="url(#wave-light)"/>
  </svg>
  <div class="brand-dot"></div>
  <div class="brand-name"><span>HOSPITAL</span><span>VISTA SERENA</span></div>
  <div class="product-name" style="top:146px">Premium Drinking Water</div>
  <div class="address" style="left:22px;top:182px">Calle Mirador 128, Villa Norte, PR 00950<br>PO Box 41870, Villa Norte, PR 00951-1870</div>
  <div class="volume" style="left:264px;top:192px">16.9 fl oz (500mL)</div>
</section>

<!-- Option 2 -->
<section class="label" style="left:145px;top:277px">
  <svg class="water" viewBox="0 0 388 216" role="img" aria-label="Blue water surface with large bubbles">
    <path d="M0 95 C90 80 160 112 240 102 C310 94 350 80 388 86 L388 216 L0 216 Z" fill="url(#wave-blue)"/>
  </svg>
  <div class="address" style="left:188px;top:8px">Calle Mirador 128, Villa Norte, PR 00950<br>PO Box 41870, Villa Norte, PR 00951-1870</div>
  <div class="brand-dot"></div>
  <div class="brand-name"><span>HOSPITAL</span><span>VISTA SERENA</span></div>
  <div class="volume" style="left:270px;top:146px">16.9 fl oz (500mL)</div>
  <div class="product-name" style="top:176px">Premium Drinking Water</div>
</section>

<!-- Option 3 -->
<section class="label" style="left:145px;top:515px">
  <svg class="water" viewBox="0 0 388 216" role="img" aria-label="Cresting blue wave full of bubbles">
    <path d="M0 112 C80 90 160 120 220 110 C250 60 300 10 360 10 C388 12 388 40 388 60 L388 216 L0 216 Z" fill="url(#wave-blue)"/>
  </svg>
  <div class="brand-dot"></div>
  <div class="brand-name"><span>HOSPITAL</span><span>VISTA SERENA</span></div>
  <div class="volume" style="left:264px;top:156px">16.9 fl oz (500mL)</div>
  <div class="product-name" style="top:176px">Premium Drinking Water</div>
</section>

<!-- Option 4 -->
<section class="label" style="left:145px;top:753px">
  <svg class="water" viewBox="0 0 388 216" role="img" aria-label="Deep blue splashing water band">
    <path d="M0 122 C80 108 160 130 240 116 C310 106 350 120 388 114 L388 216 L0 216 Z" fill="url(#wave-deep)"/>
  </svg>
  <div class="volume" style="left:270px;top:10px">16.9 fl oz (500mL)</div>
  <div class="brand-dot"></div>
  <div class="brand-name"><span>HOSPITAL</span><span>VISTA SERENA</span></div>
  <div class="product-name on-deep" style="top:177px">Premium Drinking Water</div>
</section>

<!-- Option 5 -->
<section class="label" style="left:659px;top:39px">
  <svg class="water" viewBox="0 0 388 216" role="img" aria-label="Flowing water wave turning deep blue">
    <path d="M0 118 C100 96 200 120 290 110 C340 104 370 100 388 104 L388 216 L0 216 Z" fill="url(#wave-deep)"/>
  </svg>
  <div class="brand-dot"></div>
  <div class="brand-name"><span>HOSPITAL</span><span>VISTA SERENA</span></div>
  <div class="address" style="left:84px;top:134px">Calle Mirador 128, Villa Norte, PR 00950<br>PO Box 41870, Villa Norte, PR 00951-1870</div>
  <div class="product-name on-deep" style="top:181px;font-size:16px">Premium Drinking Water 16.9 fl oz (500mL)</div>
</section>

<!-- Option 6 -->
<section class="label" style="left:659px;top:277px">
  <svg class="water" viewBox="0 0 388 216" role="img" aria-label="Dark blue rolling wave with bubbles">
    <path d="M0 104 C60 96 120 130 200 128 C280 126 330 90 388 100 L388 216 L0 216 Z" fill="url(#wave-deep)"/>
  </svg>
  <div class="address" style="left:188px;top:8px">Calle Mirador 128, Villa Norte, PR 00950<br>PO Box 41870, Villa Norte, PR 00951-1870</div>
  <div class="brand-dot"></div>
  <div class="brand-name"><span>HOSPITAL</span><span>VISTA SERENA</span></div>
  <div class="volume on-deep" style="left:264px;top:156px">16.9 fl oz (500mL)</div>
  <div class="product-name on-deep" style="top:176px">Premium Drinking Water</div>
</section>

<!-- Option 7 -->
<section class="label" style="left:659px;top:515px">
  <svg class="water" viewBox="0 0 388 216" role="img" aria-label="Clear water line with rising bubbles">
    <path d="M0 120 L388 120 L388 216 L0 216 Z" fill="url(#wave-clear)"/>
  </svg>
  <div class="volume" style="left:238px;top:14px">16.9 fl oz (500mL)</div>
  <div class="brand-dot"></div>
  <div class="brand-name"><span>HOSPITAL</span><span>VISTA SERENA</span></div>
  <div class="product-name" style="top:177px">Premium Drinking Water</div>
</section>

<!-- Option 8 -->
<section class="label" style="left:659px;top:753px">
  <svg class="water" viewBox="0 0 388 216" role="img" aria-label="Calm clear water surface with bubbles">
    <path d="M0 132 C100 120 200 126 290 124 C340 122 370 126 388 128 L388 216 L0 216 Z" fill="url(#wave-clear)"/>
  </svg>
  <div class="volume" style="left:242px;top:10px">16.9 fl oz (500mL)</div>
  <div class="brand-dot"></div>
  <div class="brand-name"><span>HOSPITAL</span><span>VISTA SERENA</span></div>
  <div class="product-name" style="top:177px">Premium Drinking Water</div>
</section>

</body>
</html>
```